Design Creative Banner or Gif Ads. 3 Designs To Be Selected

Come up with some creative banner ads for stonewell.co.nz

*At least 3 different winning banners will be chosen*

Please provide banner ads / gif ads in common google ads / website banner formats.

They can be gif or static but must stand out while still maintaining clear clean text and visuals, with a premium professional feel (please avoid clip art or anything that gives a cheap message).

Please keep in mind that these will likely be small ads so text needs to be large and if there's there a lot of text then use multiple frames/ pages as submit as a gif.

Style
Minimal & clean lines
Architectural or realistic images
Avoid cartoon styles, clipart, or anything that looks cheap

Font
Nexa or Montserrat or similar

Tone
Premium, serious, trustworthy — fits new builds

Colours
Option 1: Deep Navy (trust & quality) & lighter blues and warm grey
Option 2: Open to bright colours to help the ads stand out, such as (but not limited to) bright pink with black, yellow, fluorescent green, provided the messaging is still done professionally.
Our logo is attached (Stone Well Logo)

Display Sizes
Ad specs for file sizes should be file formats like JPEG, GIF, and PNG, with animations limited to a max of 30 seconds or less.
We will need several different ad sizes provided for each of the 3 selected winning designs.

• Medium Rectangle: 300 × 250 pixels
• Leaderboard: 728 × 90 pixels
• Desktop Banner ad image: (640x360 pixels)
• Desktop Banner ad image 2: (300x600 pixels)
• Possibly one or two other sizes

Flexibility to be creative
The ad text, words, upper/lower case, layout, colour, theme, and images can be adjusted to how you think it will look best. The follow example ads are just examples of what we are after but we are keen to see what you can create.

Recommendations at this point:
1. Avoid text heavy
2. Looking for more Gif ads
3. Imaging: if possible use real stock photo's rather than AI

Themes:

1
Building Soon? Start Here
Free Build Planning Pack:
✓ Build Cost Calculator
✓ Hidden Cost Checklist
✓ Builder Comparison Guide
Build With Confidence
Download Free

2
Before You Choose A Builder
Compare Price, Scope, Risk & Value
Avoid Costly Mistakes
Choose The Right Builder With Confidence
Download The Free Guide

3
Planning A New Build?
Avoid These Common Mistakes:
✗ Hidden Exclusions
✗ Missing Scope
✗ Unrealistic Allowances
✗ Budget Blowouts
Download The Free Guide

4
Before You Buy Land
Know what it could cost to build.
Avoid Costly Building Mistakes
Download Our Free Guides

5
Know Your Build Budget?
• Free Build Cost Calculator
• Hidden Cost Checklist
• Build Planning Tools
Calculate Costs (Download)

Target Market(s)

Landowners looking to build

Industry/Entity Type

Building

Font styles to use
Other font styles liked:
• Nexa or Montserrat or similar

Requirements
Should not have
• Avoid cartoon styles, clipart, or anything that looks cheap

```html
<!DOCTYPE html>
<html lang="en">
<head>
<meta charset="UTF-8">
<title>Stone Well – Free Build Planning Pack</title>
<link rel="stylesheet" href="https://fonts.googleapis.com/css2?family=Montserrat:wght@500;600;700;800&display=swap">
<style>
  :root {
    --navy: #0b1060;
    --navy-deep: #070b45;
    --white: #ffffff;
    --tick-blue: #3d8ff2;
    --cta-yellow: #f7c51a;
    --cta-text: #1a1a2e;
    --photo-light: #f1ede8;
    --photo-warm: #d9cfc4;
    --photo-red: #a8463c;
  }
  * { margin: 0; padding: 0; box-sizing: border-box; }
  html, body {
    width: 1200px;
    height: 675px;
    overflow: hidden;
    background: var(--navy);
  }
  .banner {
    position: relative;
    width: 1200px;
    height: 675px;
    overflow: hidden;
    background: var(--navy);
    font-family: "Montserrat", sans-serif;
    color: var(--white);
  }
  .hero-photo {
    position: absolute;
    inset: 0;
  }
  .brand {
    position: absolute;
    left: 38px;
    top: 34px;
    display: flex;
    align-items: center;
    gap: 22px;
  }
  .brand-square {
    width: 78px;
    height: 78px;
    background: var(--white);
  }
  .brand-name {
    font-size: 56px;
    font-weight: 700;
    line-height: 1;
    letter-spacing: -0.5px;
  }
  .brand-tagline {
    margin-top: 10px;
    font-size: 13.5px;
    font-weight: 700;
    letter-spacing: 0.2px;
  }
  .headline {
    position: absolute;
    left: 38px;
    top: 160px;
    font-size: 45px;
    font-weight: 800;
    letter-spacing: -0.3px;
  }
  .pack-list {
    position: absolute;
    left: 40px;
    top: 246px;
    list-style: none;
  }
  .pack-item {
    display: flex;
    align-items: center;
    gap: 20px;
    height: 34px;
    margin-bottom: 32px;
    font-size: 31px;
    font-weight: 600;
  }
  .tick { width: 34px; height: 34px; flex: none; }
  .cta {
    position: absolute;
    left: 38px;
    top: 452px;
    width: 309px;
    height: 96px;
    background: var(--cta-yellow);
    border-radius: 5px;
    display: flex;
    align-items: center;
    justify-content: center;
    gap: 16px;
    color: var(--cta-text);
    font-size: 36px;
    font-weight: 600;
    text-decoration: none;
  }
  .cta-icon { width: 38px; height: 38px; }
  .cta-note {
    position: absolute;
    left: 375px;
    top: 468px;
    font-size: 21px;
    font-weight: 500;
    line-height: 1.5;
  }
  .footer-band {
    position: absolute;
    left: 0;
    bottom: 0;
    width: 1200px;
    height: 79px;
    background: var(--navy-deep);
    padding: 8px 38px 0;
    font-size: 24px;
    font-weight: 700;
    line-height: 1.35;
    letter-spacing: 0.4px;
  }
</style>
</head>
<body>
<main class="banner">
  <svg class="hero-photo" width="1200" height="675" viewBox="0 0 1200 675">
    <defs>
      <radialGradient id="photoTone" cx="0.6" cy="0.35" r="0.75">
        <stop offset="0" stop-color="var(--photo-red)"/>
        <stop offset="0.35" stop-color="var(--photo-warm)"/>
        <stop offset="0.8" stop-color="var(--photo-light)"/>
      </radialGradient>
    </defs>
    <circle cx="1213" cy="206" r="525" fill="#ffffff"/>
    <circle cx="1213" cy="206" r="515" fill="url(#photoTone)" role="img" aria-label="Photo of hands using a calculator beside a red model house"/>
  </svg>

  <header class="brand">
    <div class="brand-square"></div>
    <div>
      <div class="brand-name">Stone Well</div>
      <div class="brand-tagline">COMPARE QUOTES FROM TRUSTED BUILDERS</div>
    </div>
  </header>

  <h1 class="headline">Free Build Planning Pack</h1>

  <ul class="pack-list">
    <li class="pack-item">
      <svg class="tick" viewBox="0 0 34 34"><circle cx="17" cy="17" r="17" fill="var(--tick-blue)"/><path d="M10 17.5l5 5 9-10" fill="none" stroke="#fff" stroke-width="3.4" stroke-linecap="round" stroke-linejoin="round"/></svg>
      Build Cost Calculator
    </li>
    <li class="pack-item">
      <svg class="tick" viewBox="0 0 34 34"><circle cx="17" cy="17" r="17" fill="var(--tick-blue)"/><path d="M10 17.5l5 5 9-10" fill="none" stroke="#fff" stroke-width="3.4" stroke-linecap="round" stroke-linejoin="round"/></svg>
      Build Journey Roadmap
    </li>
    <li class="pack-item">
      <svg class="tick" viewBox="0 0 34 34"><circle cx="17" cy="17" r="17" fill="var(--tick-blue)"/><path d="M10 17.5l5 5 9-10" fill="none" stroke="#fff" stroke-width="3.4" stroke-linecap="round" stroke-linejoin="round"/></svg>
      Hidden Cost Checklist
    </li>
  </ul>

  <a class="cta" href="#">
    <svg class="cta-icon" viewBox="0 0 38 38" fill="none" stroke="var(--cta-text)" stroke-width="3.4" stroke-linecap="round" stroke-linejoin="round">
      <path d="M19 5v20M11 17l8 8 8-8M5 26v6h28v-6"/>
    </svg>
    Download
  </a>
  <p class="cta-note">(Free Build<br>Planning Pack)</p>

  <footer class="footer-band">
    THE RIGHT BUILDER WITH CLARITY &amp;<br>CONFIDENCE. STONE WELL.
  </footer>
</main>
</body>
</html>
```